Business card for event manager / organizer "velmora tandem"

Draft of a new valuable business card for my company.
Events, personnel service providers, festivals

```html
<!DOCTYPE html>
<html lang="de">
<head>
<meta charset="utf-8">
<title>velmora tandem – Visitenkarte</title>
<link rel="stylesheet" href="https://fonts.googleapis.com/css2?family=Jost:wght@300;400;500&family=Russo+One&display=swap">
<style>
  :root {
    --backdrop: #2b2b2d;
    --card-dark: #221f21;
    --orange: #e8731f;
    --text-light: #f2eee9;
    --text-muted: #b9b2ab;
    --photo-top: #3a2f2c;
    --photo-mid: #5a3a26;
    --photo-low: #8a4f24;
  }
  * { margin: 0; padding: 0; box-sizing: border-box; }
  html, body { width: 1200px; height: 874px; overflow: hidden; }
  body {
    background: var(--backdrop);
    font-family: "Jost", sans-serif;
    display: flex;
    flex-direction: column;
    align-items: center;
    justify-content: center;
    gap: 40px;
  }
  .card {
    width: 580px;
    height: 374px;
    border-radius: 22px;
    position: relative;
    overflow: hidden;
    box-shadow: 0 10px 30px rgba(0,0,0,.45);
  }
  .card-front {
    background: var(--card-dark);
    display: flex;
    align-items: center;
    justify-content: center;
  }
  .brand { display: flex; flex-direction: column; align-items: flex-start; }
  .brand-line { display: flex; align-items: center; gap: 18px; }
  .brand-square { width: 54px; height: 54px; background: var(--orange); }
  .brand-name {
    font-family: "Jost", sans-serif;
    font-weight: 500;
    font-size: 50px;
    color: var(--text-light);
    letter-spacing: 1px;
    line-height: 1;
  }
  .brand-tagline {
    margin-top: 10px;
    margin-left: 72px;
    font-weight: 300;
    font-size: 14px;
    color: var(--text-muted);
    letter-spacing: .5px;
  }
  .card-back { color: var(--text-light); }
  .crowd-photo {
    position: absolute; inset: 0;
    background:
      radial-gradient(ellipse at 65% 30%, rgba(190,150,140,.25), transparent 55%),
      linear-gradient(180deg, var(--photo-top) 0%, var(--photo-top) 38%, var(--photo-mid) 70%, var(--photo-low) 100%);
  }
  .owner { position: absolute; left: 40px; top: 40px; }
  .owner-name {
    font-family: "Russo One", sans-serif;
    font-weight: 400;
    font-size: 27px;
    color: var(--orange);
    letter-spacing: .5px;
  }
  .owner-role { font-size: 19px; margin-top: 2px; }
  .owner-address { font-size: 17px; margin-top: 6px; }
  .contact {
    position: absolute; right: 30px; top: 150px;
    list-style: none;
  }
  .contact li {
    display: flex; align-items: center; justify-content: flex-end; gap: 12px;
    font-size: 17px; line-height: 22px;
  }
  .contact svg { width: 14px; height: 14px; flex: none; }
</style>
</head>
<body>
  <section class="card card-front">
    <div class="brand">
      <div class="brand-line">
        <span class="brand-square"></span>
        <span class="brand-name">velmora tandem</span>
      </div>
      <p class="brand-tagline">…weil jedes Fest gute Gastgeber braucht!</p>
    </div>
  </section>

  <section class="card card-back">
    <div class="crowd-photo" role="img" aria-label="Festival crowd with raised hands in warm orange stage light"></div>
    <div class="owner">
      <h1 class="owner-name">LENA MARQUARDT</h1>
      <p class="owner-role">Inhaber</p>
      <p class="owner-address">Birkenweg 12, 48155 Norden</p>
    </div>
    <ul class="contact">
      <li>02511 555 01 42
        <svg viewBox="0 0 14 14"><path d="M3 1l2.5 3-1.5 1.5c.8 1.8 2 3 3.5 3.5L9 7.5l3 2.5-1.2 2.5C6 12.5 1.5 8 1.5 3.2z" fill="var(--orange)"/></svg></li>
      <li>0170 555 29 38
        <svg viewBox="0 0 14 14"><path d="M3 1l2.5 3-1.5 1.5c.8 1.8 2 3 3.5 3.5L9 7.5l3 2.5-1.2 2.5C6 12.5 1.5 8 1.5 3.2z" fill="var(--orange)"/></svg></li>
      <li>info@velmora-tandem.de
        <svg viewBox="0 0 14 14"><rect x="1" y="3" width="12" height="8" fill="var(--orange)"/><path d="M1 3l6 4.5L13 3" stroke="var(--card-dark)" fill="none"/></svg></li>
      <li>www.velmora-tandem.de
        <svg viewBox="0 0 14 14"><circle cx="7" cy="7" r="6" fill="var(--orange)"/><path d="M1 7h12M7 1c-2.5 3-2.5 9 0 12M7 1c2.5 3 2.5 9 0 12" stroke="var(--card-dark)" fill="none" stroke-width=".9"/></svg></li>
      <li>velmora-tandem
        <svg viewBox="0 0 14 14"><circle cx="7" cy="7" r="6" fill="var(--orange)"/></svg></li>
    </ul>
  </section>
</body>
</html>
```